Dale Morrikan Plumbing and Heating

Need a card design for a plumbing and heating company that does service and repair, remodels, and plumbing in new construction. Please add following on back side of card; Boilers, Water heaters, Gas lines, Sump pumps, Toilet repairs, Faucet repairs, Pipe thawing, Radiant heating, New construction, Remodels.

Industry/Entity Type

Plumber

Contact Information for Business Card

Was thinking white gloss card with colored logo in middle or black glossy card with silver logo in middle. Just a thought but very open to other designs.

Requirements
Must have
• Need following on front of card;
• P(203) 321-8689
• C(203) 232-9069
• Dale Morrikan 275 Larkwell St West, Stamford, Ct 06214
• service@DrainHearth.example (plumbing in blue, heating in red)
• www.DrainHearth.example (plumbing in blue, heating in red)
• Fully Licensed and Insured
Nice to have
• Elegant design

```html
<!DOCTYPE html>
<html lang="en">
<head>
<meta charset="utf-8">
<title>Dale Morrikan Plumbing and Heating – Business Card</title>
<link href="https://fonts.googleapis.com/css2?family=Arimo:wght@400;700&display=swap" rel="stylesheet">
<style>
  :root {
    --stage: #2b2b2b;
    --card-black: #050505;
    --card-white: #ffffff;
    --brand-blue: #2b3fa8;
    --bright-blue: #2f7be0;
    --brand-red: #d0303a;
    --silver: #c9ccd1;
    --ink-grey: #6b6b6b;
    --text-white: #f2f2f2;
  }
  * { box-sizing: border-box; margin: 0; padding: 0; }
  html, body { width: 1200px; height: 750px; overflow: hidden; }
  body {
    background: var(--stage);
    font-family: "Arimo", Arial, sans-serif;
    display: flex;
    align-items: center;
    justify-content: center;
    gap: 48px;
  }
  .card {
    width: 525px;
    height: 300px;
    position: relative;
    overflow: hidden;
    box-shadow: 0 12px 30px rgba(0,0,0,.45);
  }

  /* Back side */
  .card-back {
    background: radial-gradient(ellipse at 60% 25%, #1c1c1c 0%, var(--card-black) 60%);
    color: var(--text-white);
    text-align: center;
  }
  .back-brand {
    position: absolute;
    top: 62px; left: 0; right: 0;
    display: flex; align-items: center; justify-content: center; gap: 12px;
  }
  .brand-dot {
    width: 14px; height: 14px; border-radius: 50%;
    background: var(--bright-blue);
  }
  .back-brand .brand-name {
    font-weight: 700; font-size: 30px; letter-spacing: 1px;
    color: var(--silver); text-transform: uppercase;
  }
  .services {
    position: absolute; top: 150px; left: 0; right: 0;
    font-size: 13.5px; line-height: 21px; color: var(--text-white);
  }
  .services .sep { color: var(--brand-blue); margin: 0 5px; }
  .licensed {
    position: absolute; top: 222px; left: 0; right: 0;
    font-size: 15px; color: var(--brand-blue);
  }
  .licensed .amp { color: var(--brand-red); }
  .back-rule {
    position: absolute; top: 250px; left: 60px; right: 60px; height: 1px;
    background: linear-gradient(90deg, transparent, var(--brand-red) 20%, var(--brand-red) 80%, transparent);
  }

  /* Front side */
  .card-front { background: var(--card-white); }
  .front-brand {
    position: absolute; top: 36px; left: 34px; width: 260px;
  }
  .front-brand .brand-row { display: flex; align-items: center; gap: 10px; }
  .front-brand .brand-name {
    font-weight: 700; font-size: 19px; line-height: 22px;
    color: var(--brand-blue); text-transform: uppercase; letter-spacing: .5px;
  }
  .front-brand .web {
    margin-top: 6px; padding-bottom: 6px; font-size: 10px;
    border-bottom: 1px solid #cfcfcf;
  }
  .blue { color: var(--brand-blue); }
  .red { color: var(--brand-red); }
  .contact {
    position: absolute; top: 150px; left: 42px;
    font-size: 13.5px; line-height: 19px; color: var(--ink-grey);
  }
  .contact .line { display: flex; align-items: center; gap: 7px; }
  .contact svg { width: 13px; height: 13px; fill: var(--brand-blue); flex: none; }
  .contact .indent { padding-left: 20px; }
  .person {
    position: absolute; top: 88px; right: 44px; text-align: right;
  }
  .person .name { font-size: 20px; font-weight: 700; color: var(--brand-blue); }
  .person .title { font-size: 14px; color: var(--brand-red); margin-top: 2px; }
  .edge-bar {
    position: absolute; top: 62px; right: 0; width: 16px; height: 40px;
    background: var(--brand-blue);
  }
</style>
</head>
<body>

  <section class="card card-back" aria-label="Card back">
    <div class="back-brand">
      <span class="brand-dot"></span>
      <span class="brand-name">Dale Morrikan</span>
    </div>
    <p class="services">
      Boilers<span class="sep">•</span>Water heaters<span class="sep">•</span>Gas lines<span class="sep">•</span>Sump pumps<br>
      Toilet repairs<span class="sep">•</span>Faucet repairs<span class="sep">•</span>Pipe thawing<span class="sep">•</span>Radiant heating<br>
      New construction<span class="sep">•</span>Remodels.
    </p>
    <p class="licensed">Fully Licensed <span class="amp">&amp;</span> Insured</p>
    <div class="back-rule"></div>
  </section>

  <section class="card card-front" aria-label="Card front">
    <div class="front-brand">
      <div class="brand-row">
        <span class="brand-name">Dale Morrikan<br>Plumbing and Heating</span>
      </div>
      <p class="web"><span class="blue">www.Drain</span><span class="red">Hearth.example</span></p>
    </div>

    <div class="contact">
      <p class="indent">Dale Morrikan</p>
      <p class="indent">275 Larkwell St West</p>
      <p class="indent">Stamford, Ct 06214</p>
      <p class="line">
        <svg viewBox="0 0 24 24"><path d="M6.6 10.8a15 15 0 0 0 6.6 6.6l2.2-2.2a1 1 0 0 1 1-.25 11.4 11.4 0 0 0 3.6.6 1 1 0 0 1 1 1V20a1 1 0 0 1-1 1A17 17 0 0 1 3 4a1 1 0 0 1 1-1h3.5a1 1 0 0 1 1 1c0 1.25.2 2.45.6 3.6a1 1 0 0 1-.25 1z"/></svg>
        (203) 555-0147
      </p>
      <p class="line">
        <svg viewBox="0 0 24 24"><path d="M7 1h10a2 2 0 0 1 2 2v18a2 2 0 0 1-2 2H7a2 2 0 0 1-2-2V3a2 2 0 0 1 2-2zm0 3v14h10V4zm5 15.5a1 1 0 1 0 0 2 1 1 0 0 0 0-2z"/></svg>
        (203) 555-0183
      </p>
      <p class="line">
        <svg viewBox="0 0 24 24"><path d="M2 5h20v14H2zm2 2v.5l8 5 8-5V7l-8 5z"/></svg>
        <span><span class="blue">service@Drain</span><span class="red">Hearth.example</span></span>
      </p>
    </div>

    <div class="person">
      <p class="name">Evan Tolliver</p>
      <p class="title">President</p>
    </div>
    <div class="edge-bar"></div>
  </section>

</body>
</html>
```